Business Card / Appointment Card for Physician

On one side it should give the logo, address, and contact information, and on the other side it should br an Appointment card.

One Side:
Logo (see attached files)
Board Certified American Orthopedic Surgery

1487 Harrowgate Ave.
Suite KM7
Bronx, NY 10527
Tel: (718) 552 - 1948
Fax: (718) 552 - 7210

628 Fourth Ave.
Suite 42
New York, NY 10087
Tel: (212) 734 - 2815

Second Side:
Appointment
give them a choice of Bronx or Mahattan office
For:
Date:
Time:

If you are unable to keep your appointment, please call (718) 263-5102 24hrs in advance.

Target Market(s)

People that need orthopedic surgery

Industry/Entity Type

Business

Contact Information for Business Card

smart and attractive

Requirements
Must have
• logo
• contact information on one side, appointment information on the other

```html
<!DOCTYPE html>
<html lang="en">
<head>
<meta charset="utf-8">
<title>Daniel R. Ashford MD PC – Business &amp; Appointment Card</title>
<link rel="stylesheet" href="https://fonts.googleapis.com/css2?family=Source+Sans+3:wght@400;600;700&display=swap">
<style>
  :root {
    --page-bg: #ece9e4;
    --card-bg: #ffffff;
    --ink: #2b2b2b;
    --ink-soft: #3d3d3d;
    --rule: #444444;
    --brand-blue: #1d6fb5;
    --brand-green: #7ab648;
    --knee-grey: #e2e2e2;
    --shoulder-green: #eef4e6;
    --knee-blue: #e6f2fa;
  }
  * { box-sizing: border-box; margin: 0; padding: 0; }
  html, body { width: 1200px; height: 900px; overflow: hidden; }
  body {
    background: var(--page-bg);
    font-family: "Source Sans 3", sans-serif;
    color: var(--ink);
    position: relative;
  }
  .card {
    position: absolute;
    top: 295px;
    width: 540px;
    height: 310px;
    background: var(--card-bg);
    box-shadow: 0 6px 18px rgba(0,0,0,.16);
    overflow: hidden;
  }
  .appointment-card { left: 40px; }
  .business-card { left: 620px; }

  /* Appointment side */
  .knee-art {
    position: absolute; left: 0; top: 0;
    width: 200px; height: 100%;
    background: linear-gradient(160deg, var(--knee-grey), #d6d6d6);
  }
  .appointment-title {
    position: absolute; top: 26px; left: 0; width: 100%;
    text-align: center; font-weight: 700; font-size: 22px; letter-spacing: .5px;
  }
  .office-choice {
    position: absolute; font-size: 18px; display: flex; align-items: center; gap: 8px;
  }
  .office-choice .box {
    width: 13px; height: 13px; border: 1.5px solid var(--ink); display: inline-block;
  }
  .office-choice.manhattan { top: 62px; left: 320px; }
  .office-choice.bronx { top: 112px; left: 60px; }
  .fill-line {
    position: absolute; height: 1px; background: var(--rule);
  }
  .fill-line.office { top: 92px; left: 190px; width: 320px; }
  .field {
    position: absolute; left: 60px; right: 30px;
    display: flex; align-items: flex-end; gap: 6px;
    font-size: 19px; font-weight: 600;
  }
  .field .line { flex: 1; height: 1px; background: var(--rule); margin-bottom: 6px; }
  .field.for { top: 140px; }
  .field.date { top: 178px; }
  .field.time { top: 216px; }
  .cancel-note {
    position: absolute; right: 30px; bottom: 30px; width: 300px;
    font-size: 12px; line-height: 1.3; color: var(--ink-soft);
  }

  /* Business side */
  .shoulder-art {
    position: absolute; left: -20px; top: 20px;
    width: 230px; height: 230px; border-radius: 50%;
    background: var(--shoulder-green);
  }
  .knee-edge-art {
    position: absolute; right: 0; top: 70px;
    width: 70px; height: 240px;
    background: linear-gradient(180deg, var(--knee-blue), #f3f9fd);
  }
  .brand {
    position: absolute; top: 28px; right: 40px; text-align: right;
  }
  .brand-name {
    display: flex; align-items: center; justify-content: flex-end; gap: 10px;
    font-size: 24px; font-weight: 600; color: var(--brand-blue); letter-spacing: .3px;
  }
  .brand-dot { width: 30px; height: 30px; border-radius: 50%; background: var(--brand-blue); }
  .board-line {
    margin-top: 8px; font-size: 14px; font-weight: 700; color: var(--ink);
  }
  .office {
    position: absolute; font-size: 18px; line-height: 1.2; color: var(--ink-soft);
  }
  .office.bronx { left: 60px; top: 168px; }
  .office.manhattan { left: 300px; top: 148px; }
  .divider {
    position: absolute; left: 280px; top: 148px; width: 1.5px; height: 120px;
    background: var(--brand-blue);
  }
  .contact { display: flex; align-items: center; gap: 6px; margin-top: 4px; }
  .contact svg { width: 18px; height: 18px; flex: none; }
  .office.manhattan .contact { margin-top: 18px; }
</style>
</head>
<body>

<section class="card appointment-card" aria-label="Appointment card">
  <div class="knee-art" role="img" aria-label="Faint knee joint illustration"></div>
  <h1 class="appointment-title">APPOINTMENT</h1>
  <div class="office-choice manhattan"><span class="box"></span>Mahattan office</div>
  <div class="fill-line office"></div>
  <div class="office-choice bronx"><span class="box"></span>Bronx Office</div>
  <div class="field for">For:<span class="line"></span></div>
  <div class="field date">Date:<span class="line"></span></div>
  <div class="field time">Time:<span class="line"></span></div>
  <p class="cancel-note">If you are unable to keep your appointment, please call (718) 263-5102 24hrs in advance.</p>
</section>

<section class="card business-card" aria-label="Business card">
  <div class="shoulder-art" role="img" aria-label="Faint shoulder joint illustration"></div>
  <div class="knee-edge-art" role="img" aria-label="Faint knee bone illustration"></div>

  <div class="brand">
    <div class="brand-name"><span class="brand-dot"></span>DANIEL R. ASHFORD MD PC</div>
    <div class="board-line">Board Certified American Orthopedic Surgery</div>
  </div>

  <address class="office bronx" style="font-style:normal">
    1487 Harrowgate Ave.<br>Suite KM7<br>Bronx, NY 10527
    <div class="contact">
      <svg viewBox="0 0 20 20" aria-hidden="true"><circle cx="10" cy="10" r="10" fill="#1d6fb5"/><path d="M6.5 5.5c.6-.5 1.3-.4 1.6.2l.8 1.6c.2.5 0 1-.4 1.3l-.5.4c.5 1.2 1.4 2.1 2.6 2.6l.4-.5c.3-.4.8-.6 1.3-.4l1.6.8c.6.3.7 1 .2 1.6-.9 1-2.3 1.2-3.6.5-2-1.1-3.5-2.6-4.5-4.5-.7-1.3-.5-2.7.5-3.6z" fill="#fff"/></svg>
      (718) 552 - 1948
    </div>
    <div class="contact">
      <svg viewBox="0 0 20 20" aria-hidden="true"><circle cx="10" cy="10" r="10" fill="#1d6fb5"/><rect x="6" y="5" width="8" height="4" fill="#fff"/><rect x="5" y="9" width="10" height="6" rx="1" fill="#fff"/><rect x="7" y="11" width="6" height="1" fill="#1d6fb5"/></svg>
      (718) 552 - 7210
    </div>
  </address>

  <div class="divider"></div>

  <address class="office manhattan" style="font-style:normal">
    628 Fourth Ave.<br>Suite 42<br>New York, NY 10087
    <div class="contact">
      <svg viewBox="0 0 20 20" aria-hidden="true"><circle cx="10" cy="10" r="10" fill="#1d6fb5"/><path d="M6.5 5.5c.6-.5 1.3-.4 1.6.2l.8 1.6c.2.5 0 1-.4 1.3l-.5.4c.5 1.2 1.4 2.1 2.6 2.6l.4-.5c.3-.4.8-.6 1.3-.4l1.6.8c.6.3.7 1 .2 1.6-.9 1-2.3 1.2-3.6.5-2-1.1-3.5-2.6-4.5-4.5-.7-1.3-.5-2.7.5-3.6z" fill="#fff"/></svg>
      (212) 734 - 2815
    </div>
  </address>
</section>

</body>
</html>
```